Coaching landingpage/salespage need a layout

Hi!
We are two people from Sweden looking for help to design our coaching landingpage/salespage.

What about:
We need a nice modern timeless appealing Photoshop layout (landingpage) for our coaching page where we coach people to “how to get a richer lifestyle”.

Style of page:
We want the site to reflect seriousness but still harmonic. We would like somewhat colorful and (but not too crazy). After all, we are coaching about investments and private economy.
Responsive layout – consider stacking order when scaling down window width. Fullpage-design where content areas are 960 grid/max-width.

----------------------------------------------------------------------------
Content on page:
*Headersection – Logo and header image with the two coaches together and space for later on adding a video.

*On the landingpage the customers can read up on what we mean by a richer lifestyle (use dummy text). We show our Trivselsnyckeln (= Lifestyle matrix) and a little description about that. If the customers want to know more, they can click "read more (or a symbolic icon that relates to read more)" to expand a hidden div (section) where they can read more about Trivselsnyckeln. They can also minimize the section.

*3-4 Unique selling points “Four reasons why choose coaching” with nice designed number-icons and some place for text.

*The customer should also be able to read something about what happens during a typical coaching session, some bullets that summarize it (use dummy text) and a couple of headlines, maybe 3 or 4 (about what they need to prepare for themselves .eg Skype, headset/microphone etc).

*Offer/product section: A section where the customer can see what services we provide, choose product and click order. When customer click order they will arrive to an order-page (this one you don’t have to design) .
Our products are as followed: Bronze (single coaching session), Silver (small-package), Gold (large-package). Use provided graphics for these products.

*Testimonials section. Currently we have 2 good testimonials, but only with text no portrait picture.

Testimonial1: “Uppiggande och inspirerande! Kommer med enkla vardagstips såväl som svårare tips. Ett roligt sätt att få en spark i baken, så att ekonomi-energin bibehålls! Tack för ett bra samtal!" - Josefin Brandeby

Testimonial2: "Värdefullast för mig var kunskapen om alternativa investeringssställen som inte är börs eller eget ägande." - Annika Sjöhalla

*Section with portraits and info about the coaches (currently 2 coaches, but in future will be several, so a design-section that’s lets us add more coaches).

*Footer-section
------------------------------------------------------------------------

Colors:
Use Trivselsnyckeln (attached file) as colorinspiration. Doesn’t have to be exactly those colors, you can use similar colors if it is more pleasing to the eye and you can also use complementary colors.

Currently we have tried of our own but don't really nail it with any apealing design. This is what we have done so far but we want to replace it with your more professional design:

https://www.harbekrona.se/full/Page/coaching13
-------------------------------------------------------------

SUMMARIZE of the above design-description:

* Our logo (attached psd-file with smart-object. You can try different colors with color-overlay)

*Apealing headerimage with portrait (attached file "big_portrait")

*Introduction text (use dummy text about 100 words)

*Text about Trivselsnyckeln (use dummy text about 200 words)

*Trivselsnyckeln (attached psd-file with smart-object)

*What we are covering during a coaching session (dummy text about 200 words and about 5 or 6 bullets)

*3-4 Unique Selling Points with stylish number icons (not 2 small) and some text.
*Our offers Bronze, Silver, Gold (attached pictures)
*Testimonials
*Picture & info about coaches (attached pictures, choose whichever suits you)
*Footer

Please comment if there are questions.

Reagards Torbjörn @ Harbe Krona

Target Market(s)

People who want to learn how to create a richer lifestyle which involves more freedom and a better well-being

Number of Pages Required

1 page

Font styles to use
Sans Serif
Other font styles liked:
• Roboto

Requirements
Should not have
• A cheezy unmodern landingpage with lots of texts and 10 sign-up buttons.
• This page is not a site about capturing emails and building lists by provide a "best-guide-for-something". It´s about getting people to book and pay for one or more coaching-sessions.

```html
<!DOCTYPE html>
<html lang="en">
<head>
<meta charset="utf-8">
<title>Harbe Krona – Coaching</title>
<link href="https://fonts.googleapis.com/css2?family=Roboto:ital,wght@0,300;0,400;0,500;0,700;1,400&display=swap" rel="stylesheet">
<style>
:root{
  --blue:#1b8bd3;
  --orange:#f0733a;
  --peach:#f8cb98;
  --text-brown:#8d7a66;
  --grey-dark:#575757;
  --white:#ffffff;
}
*{box-sizing:border-box;margin:0;padding:0}
html,body{width:1200px;height:4063px;overflow:hidden}
body{font-family:"Roboto",Arial,sans-serif;background:var(--peach);color:var(--text-brown);position:relative}
.section{position:relative;width:1200px;overflow:hidden}

/* top bar */
.top-bar{height:100px;background:linear-gradient(180deg,#3597cc,#2a86bb);display:flex;align-items:center;justify-content:center}
.brand{display:flex;align-items:center;gap:16px;color:var(--white);font-weight:300;font-size:38px;letter-spacing:6px;text-transform:uppercase}
.brand-mark{width:34px;height:34px;background:var(--white)}

/* hero */
.hero{height:496px;background:linear-gradient(180deg,#f3b97f 0%,#f6c792 60%,#f6c48e 100%)}
.hero-title{position:absolute;left:119px;top:78px;color:var(--white);font-size:24px;font-weight:500}
.hero-more{position:absolute;left:450px;top:86px;color:#fff4e4;font-size:11px}
.video{position:absolute;left:119px;top:125px;width:426px;height:236px;background:linear-gradient(160deg,#6d6f78,#2f3036);border:3px solid #2a2a2a}
.video svg{position:absolute;left:183px;top:88px}
.hero-photo{position:absolute;left:542px;top:157px;width:582px;height:339px;background:radial-gradient(ellipse at 50% 30%,#c99a7a 0%,#6a5a55 45%,#2b2a30 100%);border-radius:40% 40% 0 0/30% 30% 0 0}

/* section titles */
.title-row{position:absolute;left:0;width:1200px;display:flex;align-items:center;justify-content:center;gap:20px}
.title-row .rule{width:54px;height:2px;background:currentColor}
.title-row h2{font-size:30px;font-weight:400;letter-spacing:1px;text-transform:uppercase}

/* about */
.about{height:401px;background:linear-gradient(180deg,#f7c693,#f9cf9f)}
.about .title-row{top:82px;color:var(--orange)}
.about p{position:absolute;left:120px;top:160px;width:960px;text-align:center;font-size:14px;line-height:22px;color:var(--text-brown)}

/* matrix */
.matrix{height:737px;background:var(--orange);color:var(--white)}
.matrix .eyebrow{position:absolute;left:0;top:38px;width:1200px;text-align:center;font-size:15px;letter-spacing:1px;text-transform:uppercase}
.matrix .title-row{top:64px;color:var(--white)}
.matrix .title-row h2{font-weight:500}
.matrix-copy{position:absolute;left:122px;top:152px;width:700px;font-size:13px;line-height:19px}
.matrix-sub{position:absolute;left:122px;top:343px;font-size:14px;font-weight:700;text-transform:uppercase}
.bullets{position:absolute;left:122px;top:385px;list-style:none}
.bullets li{display:flex;align-items:center;gap:18px;height:29.5px;font-size:13px}
.matrix-chart{position:absolute;left:832px;top:154px;width:252px;height:195px;background:linear-gradient(135deg,#f4f4f4 0%,#7fc3e8 35%,#f5c24a 55%,#8a7f74 75%,#7dc57d 100%);border:4px solid var(--white)}
.expand{position:absolute;left:122px;top:602px}

/* why */
.why{height:623px;background:linear-gradient(180deg,#f9cd9d,#f8c896)}
.why .title-row{top:58px;color:var(--orange)}
.usp{position:absolute;top:195px;width:284px;height:347px;border:2px solid #f9dcbd;text-align:center}
.usp.active{border-color:#5fa8dc}
.usp-num{position:absolute;left:105px;top:-34px;width:70px;height:70px;border-radius:50%;background:var(--white);color:var(--blue);font-size:38px;font-weight:700;line-height:70px}
.usp.active .usp-num{background:var(--blue);color:var(--white)}
.usp h3{margin-top:68px;color:var(--blue);font-size:18px;font-weight:700;text-transform:uppercase}
.usp .bar{width:60px;height:2px;background:var(--blue);margin:16px auto 22px}
.usp p{padding:0 30px;font-size:14px;line-height:22px;color:var(--text-brown)}

/* testimonial */
.testimonial{height:338px;background:var(--white);text-align:center}
.testimonial svg{position:absolute;left:572px;top:50px}
.testimonial blockquote{position:absolute;left:195px;top:142px;width:810px;font-size:19px;line-height:30px;font-style:italic;color:#7b7b7b}
.testimonial cite{position:absolute;left:0;top:260px;width:1200px;display:block;text-align:center;font-style:normal;font-size:21px;color:#333}

/* pricing */
.pricing{height:521px;background:linear-gradient(180deg,#f8cb98,#f7c591)}
.plan{position:absolute;top:63px;width:298px;height:392px;background:var(--white);text-align:center}
.medal{width:110px;height:110px;border-radius:50%;margin:46px auto 0}
.medal.bronze{background:radial-gradient(circle at 40% 35%,#e9a36b,#b8652b 70%,#8c4a1d)}
.medal.silver{background:radial-gradient(circle at 40% 35%,#f1f1f1,#b5b5b5 70%,#8d8d8d)}
.medal.gold{background:radial-gradient(circle at 40% 35%,#ffe27a,#e2ad23 70%,#b9861a)}
.plan-band{margin-top:21px;height:54px;background:var(--blue);color:var(--white);font-size:25px;font-weight:700;line-height:54px;text-transform:uppercase}
.plan-info{margin-top:32px;font-size:15px;line-height:27px;color:#6f6f6f}
.plan-btn{display:block;width:244px;height:50px;margin:16px auto 0;background:var(--grey-dark);color:var(--white);font-size:14px;line-height:50px;text-transform:uppercase}

/* coaches */
.coaches{height:346px;display:flex}
.coach{position:relative;width:600px;height:346px;color:var(--white)}
.coach.left{background:var(--orange)}
.coach.right{background:var(--blue)}
.coach-photo{position:absolute;top:27px;width:110px;height:110px;border-radius:50%;border:4px solid var(--white);background:linear-gradient(160deg,#c9a58e,#5b5049)}
.coach h3{position:absolute;top:50px;font-size:22px;font-weight:500;text-transform:uppercase;white-space:nowrap}
.coach .mail{position:absolute;top:82px;font-size:14px}
.coach p{position:absolute;top:150px;width:440px;font-size:13px;line-height:20px}
.left .coach-photo{left:155px}.left h3,.left .mail{left:290px}.left p{left:122px}
.right .coach-photo{left:32px}.right h3,.right .mail{left:167px}.right p{left:42px}

/* footer */
.footer{height:501px;background:linear-gradient(180deg,#707070,#626262);color:var(--white)}
.footer .brand{position:absolute;top:76px;left:0;width:1200px;justify-content:center}
.footer .brand-rule{position:absolute;top:138px;left:560px;width:80px;height:2px;background:#9a9a9a}
.foot-col{position:absolute;top:233px}
.foot-col h4{font-size:15px;font-weight:700;letter-spacing:1.5px;text-transform:uppercase;margin-bottom:18px}
.foot-links{list-style:none;font-size:14px;line-height:28px}
.foot-links li::before{content:"";display:inline-block;width:11px;height:11px;background:var(--white);margin-right:14px}
.foot-contact{font-size:15px;line-height:23px;letter-spacing:.5px}
.feed{position:absolute;left:856px;top:192px;width:225px;height:223px;background:var(--white);border:4px solid #ddd;color:#444;padding:10px}
.feed-head{display:flex;align-items:center;gap:8px;font-size:11px}
.feed-head span{width:34px;height:34px;background:#3b5998}
.feed small{display:block;font-size:9px;margin:10px 0 6px}
.feed-faces{height:120px;background:linear-gradient(135deg,#b49683,#5e6f85,#c7a98f,#4b4b4b)}
.foot-note{position:absolute;left:122px;top:431px;font-size:14px;font-weight:500}
.foot-copy{position:absolute;left:122px;top:458px;font-size:11px;color:#cfcfcf}
</style>
</head>
<body>

<header class="section top-bar">
  <div class="brand"><span class="brand-mark"></span>Harbe Krona</div>
</header>

<section class="section hero">
  <h1 class="hero-title">Lorem ipsum dolor sit</h1>
  <span class="hero-more">See More Videos</span>
  <div class="video" role="img" aria-label="Video still of a coaching seminar audience">
    <svg width="60" height="60" viewBox="0 0 60 60"><circle cx="30" cy="30" r="27" fill="none" stroke="#fff" stroke-width="3"/><path d="M24 18 L42 30 L24 42 Z" fill="#fff"/></svg>
  </div>
  <div class="hero-photo" role="img" aria-label="Portrait of the two coaches standing together"></div>
</section>

<section class="section about">
  <div class="title-row"><span class="rule"></span><h2>About us</h2><span class="rule"></span></div>
  <p>Sed ut perspiciatis unde omnis iste natus error sit voluptatem accusantium doloremque laudantium, totam rem aperiam, eaque ipsa quae ab illo inventore veritatis et quasi architecto beatae vitae dicta sunt explicabo. Nemo enim ipsam voluptatem quia voluptas sit aspernatur aut odit aut fugit, sed quia consequuntur magni dolores eos qui ratione voluptatem sequi nesciunt. Neque porro quisquam est, qui dolorem ipsum quia dolor sit amet, consectetur, adipisci velit, sed quia non numquam eius modi tempora incidunt ut labore et dolore magnam aliquam quaerat voluptatem. Ut enim ad minima veniam, quis nostrum exercitationem ullam corporis suscipit laboriosam adipisci velit, sed quia non numquam eius modi tempora incidunt ut labore et dolore magnam aliquam quaerat voluptatem. Ut enim ad minima veniam, quis nostrum.</p>
</section>

<section class="section matrix">
  <div class="eyebrow">Introducing</div>
  <div class="title-row"><span class="rule"></span><h2>Trivselsnyckeln</h2><span class="rule"></span></div>
  <p class="matrix-copy">Sed ut perspiciatis unde omnis iste natus error sit voluptatem accusantium doloremque laudantium, totam rem aperiam, eaque ipsa quae ab illo inventore veritatis et quasi architecto beatae vitae dicta sunt explicabo. Nemo enim ipsam voluptatem quia voluptas sit aspernatur aut odit aut fugit, sed quia consequuntur magni dolores eos qui ratione voluptatem sequi nesciunt. Neque porro quisquam est, qui dolorem ipsum quia dolor sit amet, consectetur, nisi ut aliquid ex ea commodi consequatur? Quis autem vel eum iure reprehenderit qui in ea voluptate velit esse quam nihil molestiae consequatur, vel illum qui dolorem eum fugiat quo voluptas nulla pariatur.</p>
  <div class="matrix-chart" role="img" aria-label="Trivselsnyckeln lifestyle matrix diagram with four coloured quadrants"></div>
  <h3 class="matrix-sub">Lorem ipsum dolor sit amet, consectetur</h3>
  <ul class="bullets">
    <li><svg width="18" height="14" viewBox="0 0 18 14"><path d="M1 7 L6 12 L17 1" fill="none" stroke="#fff" stroke-width="2.5"/></svg>minim veniam, quis nostrud exercitation ullamco laboris nisi ut aliquip ex ea commodo</li>
    <li><svg width="18" height="14" viewBox="0 0 18 14"><path d="M1 7 L6 12 L17 1" fill="none" stroke="#fff" stroke-width="2.5"/></svg>minim veniam, quis nostrud exercitation ullamco laboris nisi ut aliquip ex ea commodo</li>
    <li><svg width="18" height="14" viewBox="0 0 18 14"><path d="M1 7 L6 12 L17 1" fill="none" stroke="#fff" stroke-width="2.5"/></svg>minim veniam, quis nostrud exercitation ullamco laboris</li>
    <li><svg width="18" height="14" viewBox="0 0 18 14"><path d="M1 7 L6 12 L17 1" fill="none" stroke="#fff" stroke-width="2.5"/></svg>minim veniam, quis nostrud exercitation ullamco laboris nisi ut aliquip ex ea commodo</li>
    <li><svg width="18" height="14" viewBox="0 0 18 14"><path d="M1 7 L6 12 L17 1" fill="none" stroke="#fff" stroke-width="2.5"/></svg>minim veniam, quis nostrud exercitation ullamco laboris nisi ut aliquip</li>
    <li><svg width="18" height="14" viewBox="0 0 18 14"><path d="M1 7 L6 12 L17 1" fill="none" stroke="#fff" stroke-width="2.5"/></svg>minim veniam, quis nostrud exercitation ullamco laboris nisi ut aliquip ex ea commodo</li>
  </ul>
  <svg class="expand" width="50" height="50" viewBox="0 0 50 50" aria-label="Read more"><circle cx="25" cy="25" r="23" fill="none" stroke="#fff" stroke-width="2.5"/><path d="M25 14 V36 M14 25 H36" stroke="#fff" stroke-width="2.5"/></svg>
</section>

<section class="section why">
  <div class="title-row"><span class="rule"></span><h2>Why hire us</h2><span class="rule"></span></div>
  <article class="usp" style="left:122px">
    <div class="usp-num">1</div>
    <h3>Greater clarity</h3><div class="bar"></div>
    <p>Through coaching you will obtain greater clarity in what you want, why you want it and how you can achieve it. This will also stimulate you to start acting more in line with the life you really want to live.</p>
  </article>
  <article class="usp active" style="left:458px">
    <div class="usp-num">2</div>
    <h3>Better results</h3><div class="bar"></div>
    <p>Your coach will motivate and help you take continuous steps forward, closer to the results you want to achieve. In this way, begins a new life is created for you and it becomes more natural to make progress than to stand still.</p>
  </article>
  <article class="usp" style="left:794px">
    <div class="usp-num">3</div>
    <h3>Greater freedom</h3><div class="bar"></div>
    <p>Together with your coach you see that you make a lifestyle journey where you feel good and have fun while you build up a money machine for life. A money machine that can open up more freedom to do what you want.</p>
  </article>
</section>

<section class="section testimonial">
  <svg width="56" height="56" viewBox="0 0 56 56"><circle cx="28" cy="28" r="28" fill="#1b8bd3"/><path d="M17 32 q0-10 8-13 v4 q-4 2-4 5 h4 v8 h-8 z M31 32 q0-10 8-13 v4 q-4 2-4 5 h4 v8 h-8 z" fill="#fff"/></svg>
  <blockquote>Uppiggande och inspirerande! Kommer med enkla vardagstips såväl som svårare tips. Ett roligt sätt att få en spark i baken, så att ekonomi-energin bibehålls! Tack för ett bra samtal!”</blockquote>
  <cite>Josefin Brandeby</cite>
</section>

<section class="section pricing">
  <article class="plan" style="left:119px">
    <div class="medal bronze" role="img" aria-label="Bronze medal"></div>
    <div class="plan-band">Bronze</div>
    <p class="plan-info">Includes 1 session<br>Price 650 SEK</p>
    <span class="plan-btn">Make an appoinment</span>
  </article>
  <article class="plan" style="left:450px">
    <div class="medal silver" role="img" aria-label="Silver medal"></div>
    <div class="plan-band">Silver</div>
    <p class="plan-info">Includes 5 sessions<br>Price 3050 SEK</p>
    <span class="plan-btn">Make an appoinment</span>
  </article>
  <article class="plan" style="left:780px">
    <div class="medal gold" role="img" aria-label="Gold medal"></div>
    <div class="plan-band">Gold</div>
    <p class="plan-info">Includes 10 sessions<br>Price 5800 SEK</p>
    <span class="plan-btn">Make an appoinment</span>
  </article>
</section>

<section class="section coaches">
  <article class="coach left">
    <div class="coach-photo" role="img" aria-label="Portrait of coach Lennart Åkerberg"></div>
    <h3>Lennart Åkerberg</h3>
    <span class="mail">lennart@harbekrona.se</span>
    <p>Lennart has a broad background in finance and IT. As an investor his focus on dividend stocks, real estate and internet-based entrepreneurship. He also has a long experience and a passion to help people and businesses to evolve in different ways. Basically this has always been about creating more good days in life.</p>
  </article>
  <article class="coach right">
    <div class="coach-photo" role="img" aria-label="Portrait of coach Torbjörn Hedlund"></div>
    <h3>Torbjörn Hedlund</h3>
    <span class="mail">torbjorn@harbekrona.se</span>
    <p>Versatile investors with a focus on alternative and high-risk investments. Besides the stock market, investing in unlisted Swedish startup companies and various internet-based investments such as P2P lending, online games and apps.</p>
  </article>
</section>

<footer class="section footer">
  <div class="brand"><span class="brand-mark"></span>Harbe Krona</div>
  <div class="brand-rule"></div>
  <div class="foot-col" style="left:122px">
    <h4>Quick links</h4>
    <ul class="foot-links"><li>Blog</li><li>Coaching</li><li>About Us</li></ul>
  </div>
  <div class="foot-col" style="left:360px">
    <h4>Contact us</h4>
    <p class="foot-contact">Harbe Krona AB<br>Linden Road 12<br>411 06 Gothenburg</p>
  </div>
  <div class="feed">
    <div class="feed-head"><span></span>Harbe Krona on social</div>
    <small>28 people like Harbe Krona</small>
    <div class="feed-faces" role="img" aria-label="Grid of follower profile thumbnails"></div>
  </div>
  <p class="foot-note">For questions, contact us at team@harbekrona.se</p>
  <p class="foot-copy">Copyright 2015 Harbe Krona AB</p>
</footer>

</body>
</html>
```